Tick Tock Green Frog

I'm looking for one generic business card that be used for four people or would it be easier to get four different design of cards.

I have attached the logo, of the cow. I would also like to use one colour of the cow's legs in the background.

Info for card:
Dana Holcroft
Director of Programs
Phone: 044 718 2094
email: dana.holcroft@ticktockgreenfrogs.com.au
Web: www.ticktockgreenfrogs.com.au

Here is some tag lines that could also be used:

"Guiding you in the right direction"

"Putting the Tick Tock back into early childhood"
"Where there is NO fuss"

Industry/Entity Type

Business

```html
<!DOCTYPE html>
<html lang="en">
<head>
<meta charset="utf-8">
<title>Tick Tock Green Frog – Business Card</title>
<link href="https://fonts.googleapis.com/css2?family=Lato:wght@400;700&display=swap" rel="stylesheet">
<style>
  :root {
    --stage: #2b2b2b;
    --forest: #1b6e36;
    --forest-deep: #135a2a;
    --forest-glow: #2f9a4c;
    --lime: #8cc63f;
    --leaf: #5f9e3b;
    --paper: #ffffff;
    --brand-brown: #4a2812;
    --accent-orange: #f29a1f;
  }
  * { box-sizing: border-box; margin: 0; padding: 0; }
  html, body {
    width: 1200px; height: 926px; overflow: hidden;
    background: var(--stage);
    font-family: "Lato", Arial, sans-serif;
  }
  .canvas {
    width: 1200px; height: 926px;
    display: flex; flex-direction: column;
    align-items: center; justify-content: center; gap: 24px;
  }
  .card {
    position: relative;
    width: 760px; height: 434px;
    overflow: hidden;
    border-radius: 4px;
  }
  /* Front */
  .card--front { background: var(--paper); }
  .card__art { position: absolute; inset: 0; }
  .contact {
    position: absolute; left: 48px; top: 138px;
    color: var(--paper);
  }
  .contact__name { font-size: 32px; font-weight: 400; letter-spacing: .3px; }
  .contact__title { font-size: 20px; margin-top: 4px; }
  .contact__list { list-style: none; margin-top: 30px; font-size: 18px; line-height: 1.45; }
  .brand {
    position: absolute; left: 410px; top: 92px;
    display: flex; flex-direction: column; align-items: flex-start;
  }
  .brand__row { display: flex; align-items: center; gap: 12px; }
  .brand__dot { width: 26px; height: 26px; border-radius: 50%; background: var(--forest); }
  .brand__name { font-size: 30px; font-weight: 700; color: var(--brand-brown); }
  .brand__descriptor {
    margin-top: 6px; margin-left: 38px;
    font-size: 14px; font-weight: 700; color: var(--accent-orange);
  }
  /* Back */
  .card--back {
    background: radial-gradient(ellipse at 50% 30%, var(--forest-glow) 0%, var(--forest) 45%, var(--forest-deep) 100%);
    display: flex; align-items: center; justify-content: center;
  }
  .taglines {
    list-style: none; text-align: center;
    color: var(--paper); font-size: 25px; line-height: 1.3;
    margin-top: -40px;
  }
</style>
</head>
<body>
<main class="canvas">
  <section class="card card--front" aria-label="Business card front">
    <svg class="card__art" viewBox="0 0 760 434" aria-hidden="true">
      <path fill="var(--forest)" d="M0,0 L120,0 C250,40 330,150 420,250 C500,330 600,360 760,330 L760,434 L0,434 Z"/>
      <path fill="var(--lime)" d="M120,0 C250,40 330,150 420,250 C500,330 600,360 760,330 L760,318 C600,350 505,318 430,240 C345,150 260,30 150,0 Z"/>
      <path fill="var(--paper)" d="M440,434 C560,380 660,360 760,360 L760,374 C660,376 570,396 480,434 Z"/>
      <path fill="var(--lime)" d="M480,434 C570,396 660,376 760,374 L760,396 C670,396 600,412 540,434 Z"/>
      <path fill="var(--leaf)" d="M540,434 C600,412 670,396 760,396 L760,434 Z"/>
    </svg>
    <div class="contact">
      <h1 class="contact__name">Dana Holcroft</h1>
      <p class="contact__title">Director of Programs</p>
      <ul class="contact__list">
        <li>phone: 044 718 2094</li>
        <li>web: www.ticktockgreenfrogs.com.au</li>
        <li>email: dana.holcroft@ticktockgreenfrogs.com.au</li>
      </ul>
    </div>
    <div class="brand">
      <div class="brand__row">
        <span class="brand__dot"></span>
        <span class="brand__name">Tick Tock Green Frog</span>
      </div>
      <span class="brand__descriptor">practical support for early learning</span>
    </div>
  </section>

  <section class="card card--back" aria-label="Business card back">
    <ul class="taglines">
      <li>Guiding you in the right direction</li>
      <li>Putting the Tick Tock back into early childhood</li>
      <li>Where there is NO fuss</li>
    </ul>
  </section>
</main>
</body>
</html>
```